Website

I have a client that we built a website for about 10 years ago - https://www.quorvelbrightmoss.com.au/

We would like a fresh new design for it that looks more modern. All the elements, info that's on there needs to be the same but the whole design/layout needs to be modernised.

```html
<!DOCTYPE html>
<html lang="en">
<head>
<meta charset="utf-8">
<title>Quorvel Brightmoss – Custom Nametags & Badges</title>
<link href="https://fonts.googleapis.com/css2?family=Poppins:ital,wght@0,400;0,500;0,600;0,700;0,800;1,400&display=swap" rel="stylesheet">
<style>
:root{
  --red:#d3171f;
  --red-dark:#a80f16;
  --ink:#111111;
  --text:#2a2a2a;
  --muted:#666666;
  --line:#e3e3e6;
  --soft:#f3f4f6;
  --bar:#141414;
  --stage:#bdbdbd;
  --white:#ffffff;
}
*{margin:0;padding:0;box-sizing:border-box}
html,body{width:681px;height:1200px;overflow:hidden;background:var(--stage)}
body{font-family:"Poppins",sans-serif;color:var(--text)}
.page{position:absolute;left:22px;top:0;width:637px;height:1200px;background:var(--white);overflow:hidden}

/* top bar */
.topbar{height:16px;background:var(--bar);color:#ddd;font-size:4.4px;display:flex;align-items:center;justify-content:space-between;padding:0 53px}
.topbar .right{display:flex;gap:5px;align-items:center}
.pill{border:0.5px solid #555;border-radius:6px;padding:1px 4px}
.pill b{color:var(--white)}

/* nav */
.nav{height:25px;display:flex;align-items:center;justify-content:space-between;padding:0 53px;border-bottom:0.5px solid var(--line)}
.brand{display:flex;align-items:center;gap:3px;font-size:6.5px;font-weight:700;color:var(--red);line-height:1}
.brand .dot{width:7px;height:7px;border-radius:50%;background:var(--red)}
.menu{display:flex;gap:10px;font-size:4.6px;color:#444}
.menu .active{color:var(--red);border-bottom:0.7px solid var(--red);padding-bottom:1px}
.actions{display:flex;gap:4px}
.btn-login{font-size:5px;font-weight:600;border:0.5px solid var(--line);border-radius:2px;padding:3px 5px;color:var(--ink)}
.btn-build{font-size:5px;font-weight:600;background:var(--red);color:var(--white);border-radius:2px;padding:3px 5px}

/* hero */
.hero{position:relative;height:276px;background:linear-gradient(100deg,#0d0d0d 0%,#2a2a2a 45%,#4a4a4a 100%);color:var(--white)}
.hero-visual{position:absolute;right:0;top:20px;width:305px;height:240px;background:radial-gradient(ellipse at 60% 45%,#d8d8d8 0%,#9a9a9a 35%,#b8262c 55%,#3a3a3a 80%,transparent 100%);opacity:.85;border-radius:12px}
.hero-copy{position:absolute;left:44px;top:46px}
.hero h1{font-size:27px;font-weight:700;line-height:1.12;letter-spacing:-.3px}
.hero p{font-size:11px;line-height:1.5;margin-top:10px;font-weight:400;color:#eee}
.hero-btns{display:flex;gap:9px;margin-top:22px}
.hero-btns span{display:inline-flex;align-items:center;justify-content:center;height:29px;font-size:8.5px;font-weight:600;border-radius:2px}
.b-red{background:var(--red);width:102px}
.b-ghost{border:0.8px solid #ddd;width:103px}
.hero .made{font-size:7px;font-weight:600;margin-top:20px;margin-left:2px;letter-spacing:.2px}

/* sections */
.section{position:relative;padding:0 44px}
.why{height:260px;padding-top:36px}
.products{height:254px;background:var(--soft);padding-top:30px}
.sec-title{text-align:center;font-weight:800;color:var(--ink);line-height:1}
.why .sec-title{font-size:25px;letter-spacing:.3px}
.products .sec-title{font-size:25px}
.rule{width:49px;height:3.5px;background:var(--red);margin:7px auto 0;border-radius:1px}
.cards{display:grid;grid-template-columns:repeat(4,128px);gap:12px;margin-top:12px}
.card{height:136px;background:var(--white);border:0.6px solid var(--line);border-radius:3px;text-align:center;overflow:hidden}
.card .shot{height:69px;background:linear-gradient(180deg,#f4f4f4,#dcdcdc)}
.shot.red{background:linear-gradient(135deg,#eeeeee 0%,#c9c9c9 55%,#c7252c 100%)}
.shot.gold{background:radial-gradient(circle at 55% 40%,#f2c23a 0%,#c9c9c9 45%,#eeeeee 100%)}
.shot.dark{background:linear-gradient(180deg,#eeeeee 0%,#2a2a2a 30%,#2a2a2a 80%,#eeeeee 100%)}
.shot.silver{background:linear-gradient(180deg,#eeeeee 0%,#bcbcbc 50%,#c52028 85%,#eeeeee 100%)}
.card h3{font-size:8.3px;font-weight:600;color:var(--ink);margin-top:8px}
.card p{font-size:6px;color:var(--muted);line-height:1.5;margin:2px 8px 0;height:18px}
.card .cta{display:inline-block;margin-top:5px;background:var(--red);color:var(--white);font-size:5.6px;font-weight:600;padding:4px 7px;border-radius:1px}

/* testimonials & news */
.feed{height:228px;padding-top:32px;display:grid;grid-template-columns:268px 268px;gap:12px}
.feed h2{font-size:18px;font-weight:700;color:var(--ink);line-height:1;height:20px}
.news-head{display:flex;justify-content:space-between;align-items:center}
.arrows{display:flex}
.arrows span{width:16px;height:15px;border:0.5px solid var(--line);display:flex;align-items:center;justify-content:center;background:var(--white)}
.testimonial{margin-top:12px;height:101px;border:0.6px solid var(--line);border-radius:4px;padding:12px 14px;display:flex;gap:11px;position:relative}
.portrait{width:70px;height:76px;background:linear-gradient(160deg,#8a9aa6,#3a3a3a);flex:none}
.quote{font-size:6px;line-height:1.7;color:#333}
.stars{display:flex;gap:2px;margin-top:4px}
.who{font-size:7px;font-weight:600;color:var(--ink);margin-top:5px}
.org{font-size:5.6px;color:#444;margin-top:2px}
.testimonial .arrows{position:absolute;right:8px;bottom:11px}
.news{margin-top:12px;display:flex;flex-direction:column;gap:12px}
.post{height:56px;border:0.6px solid var(--line);border-radius:4px;display:flex;overflow:hidden}
.post .thumb{width:87px;flex:none;background:linear-gradient(135deg,#e9e9e9,#9a9a9a)}
.post .thumb.pens{background:linear-gradient(135deg,#2b3c78,#c52028 55%,#e3c84a)}
.post .body{padding:6px 9px}
.post h4{font-size:7px;font-weight:600;color:#222}
.post p{font-size:5.6px;line-height:1.55;color:#333;margin-top:2px}
.post time{display:block;font-size:5.6px;font-style:italic;color:#333;margin-top:2px}

/* footer */
.footer{position:relative;height:141px;background:linear-gradient(100deg,#3b1315 0%,#6a1c1f 55%,#983034 100%);border-top:4px solid var(--red);color:var(--white)}
.col{position:absolute;top:30px;font-size:7.3px;line-height:1.75}
.col h5{font-size:8.3px;font-weight:600;margin-bottom:6px}
.col li{list-style:none;display:flex;align-items:center;gap:3px}
.col li svg{flex:none}
.signup{position:absolute;left:506px;top:30px;width:92px;text-align:center}
.signup h5{font-size:7px;font-weight:500;margin-bottom:6px;text-align:left}
.signup .field{height:16px;background:var(--white);border-radius:1px;font-size:5.5px;color:#999;text-align:left;padding:4px 5px}
.signup .go{display:inline-block;margin-top:6px;background:var(--red);font-size:6px;font-weight:600;padding:3px 9px;border-radius:1px}
.social{display:flex;gap:5px;justify-content:center;margin-top:5px;padding-right:8px}
.social span{width:10px;height:10px;border-radius:50%;border:1.2px solid var(--white)}
.legal{position:absolute;left:0;right:0;bottom:0;height:18px;border-top:0.5px solid rgba(255,255,255,.2);display:flex;justify-content:center;gap:16px;align-items:center;font-size:4.6px;color:#e8dada}
</style>
</head>
<body>
<div class="page">
  <div class="topbar">
    <div>Phone: 1300 555 014 &nbsp;•&nbsp; info@quorvelbrightmoss.com.au</div>
    <div class="right"><span class="pill">Free postage over <b>$400</b></span><span>Payment</span><span>My account</span></div>
  </div>

  <header class="nav">
    <div class="brand"><span class="dot"></span>Quorvel Brightmoss</div>
    <nav class="menu">
      <span class="active">Home</span><span>Products</span><span>Price list</span><span>Trade info</span><span>FAQs</span><span>Artwork requirements</span><span>Payment</span><span>Contact</span>
    </nav>
    <div class="actions"><span class="btn-login">Login</span><span class="btn-build">Build a badge</span></div>
  </header>

  <section class="hero">
    <div class="hero-visual" role="img" aria-label="Assorted metal name badges and smiley button pins on a dark wooden table"></div>
    <div class="hero-copy">
      <h1>High-Quality Custom<br>Nametags &amp; Badges</h1>
      <p>Australia's leading supplier of professional<br>name badges and ID solutions.</p>
      <div class="hero-btns"><span class="b-red">BUILD A BADGE</span><span class="b-ghost">VIEW PRODUCTS</span></div>
      <div class="made">PROUDLY MADE IN AUSTRALIA</div>
    </div>
  </section>

  <section class="section why">
    <h2 class="sec-title">WHY CHOOSE US</h2>
    <div class="rule"></div>
    <div class="cards">
      <div class="card"><div class="shot red" role="img" aria-label="Full colour printed name badge"></div><h3>Full Colour Name Badges</h3><p>Professional badges with accurate full-colour logo reproduction.</p><span class="cta">VIEW PRODUCTS</span></div>
      <div class="card"><div class="shot gold" role="img" aria-label="Button pins with smiley designs"></div><h3>Fast turnaround</h3><p>Reliable production timelines and shipping Australia-wide.</p><span class="cta">GET A QUOTE</span></div>
      <div class="card"><div class="shot dark" role="img" aria-label="Reusable black name badge"></div><h3>Reusable Name Badges</h3><p>Ideal for staff turnover, conferences and events.</p><span class="cta">VIEW PRODUCTS</span></div>
      <div class="card"><div class="shot silver" role="img" aria-label="Engraved silver name badge with red band"></div><h3>Engraved Name Badges</h3><p>Classic engraved badges for a clean professional look.</p><span class="cta">VIEW PRODUCTS</span></div>
    </div>
  </section>

  <section class="section products">
    <h2 class="sec-title">Our Products</h2>
    <div class="rule"></div>
    <div class="cards">
      <div class="card"><div class="shot" role="img" aria-label="Full colour name badge with staff photo"></div><h3>Full Colour Name Badges</h3><p>Best for branding and logo accuracy.</p><span class="cta">VIEW PRODUCTS</span></div>
      <div class="card"><div class="shot red" role="img" aria-label="Red and white button badges"></div><h3>Photo ID Cards</h3><p>Custom cards with accessories available.</p><span class="cta">VIEW PRODUCTS</span></div>
      <div class="card"><div class="shot" role="img" aria-label="Membership card with member photo"></div><h3>Membership / Gift Cards</h3><p>High quality cards with optional finishes.</p><span class="cta">VIEW PRODUCTS</span></div>
      <div class="card"><div class="shot silver" role="img" aria-label="Silver photo badge with red accent"></div><h3>Lapel Pins</h3><p>Custom pins for awareness and branding.</p><span class="cta">VIEW PRODUCTS</span></div>
    </div>
  </section>

  <section class="section feed">
    <div>
      <h2>Testimonials</h2>
      <div class="testimonial">
        <div class="portrait" role="img" aria-label="Portrait of the reviewing customer"></div>
        <div>
          <p class="quote">“I thought I'd send a quick note to say thank you for the great service… prompt delivery of the badge I ordered.”</p>
          <div class="stars">
            <svg width="38" height="7" viewBox="0 0 38 7"><g fill="#d3171f"><path id="st" d="M3.5 0l1 2.3 2.5.2-1.9 1.6.6 2.5-2.2-1.3-2.2 1.3.6-2.5L0 2.5l2.5-.2z"/><use href="#st" x="7.7"/><use href="#st" x="15.4"/><use href="#st" x="23.1"/><use href="#st" x="30.8"/></g></svg>
          </div>
          <div class="who">Delphine</div>
          <div class="org">Fernvale Living Group</div>
        </div>
        <div class="arrows">
          <span><svg width="5" height="6" viewBox="0 0 5 6"><path d="M4 .5L1.5 3 4 5.5" fill="none" stroke="#333" stroke-width=".6"/></svg></span>
          <span><svg width="5" height="6" viewBox="0 0 5 6"><path d="M1 .5L3.5 3 1 5.5" fill="none" stroke="#333" stroke-width=".6"/></svg></span>
        </div>
      </div>
    </div>
    <div>
      <div class="news-head">
        <h2>Latest News</h2>
        <div class="arrows">
          <span><svg width="5" height="6" viewBox="0 0 5 6"><path d="M4 .5L1.5 3 4 5.5" fill="none" stroke="#333" stroke-width=".6"/></svg></span>
          <span><svg width="5" height="6" viewBox="0 0 5 6"><path d="M1 .5L3.5 3 1 5.5" fill="none" stroke="#333" stroke-width=".6"/></svg></span>
        </div>
      </div>
      <div class="news">
        <article class="post"><div class="thumb" role="img" aria-label="Assorted name badges on a desk"></div><div class="body"><h4>Tips for Designing Effective Name Badges</h4><p>When it comes to name badges, tags, and other ID products, there’s no service more trusted.</p><time>November 20, 2025</time></div></article>
        <article class="post"><div class="thumb pens" role="img" aria-label="Colourful markers and magnetic badge backs"></div><div class="body"><h4>The Benefits of Magnetic Name Badges</h4><p>Tags, and other ID products, there’s no service more trusted in Australia than Quorvel Brightmoss.</p><time>November 20, 2025</time></div></article>
      </div>
    </div>
  </section>

  <footer class="footer">
    <div class="col" style="left:50px"><h5 style="margin-left:6px">Products</h5><ul>
      <li><svg width="6" height="6" viewBox="0 0 6 6"><circle cx="3" cy="3" r="2.6" fill="none" stroke="#fff" stroke-width=".5"/><path d="M.4 3h5.2M3 .4c-1.4 1.6-1.4 3.6 0 5.2M3 .4c1.4 1.6 1.4 3.6 0 5.2" fill="none" stroke="#fff" stroke-width=".5"/></svg>Digital Services</li>
      <li style="padding-left:9px">Custom Solutions</li><li style="padding-left:9px">Platform Bridges</li><li style="padding-left:9px">Identity Cards</li></ul></div>
    <div class="col" style="left:140px"><h5 style="margin-left:9px">Company</h5><ul>
      <li><svg width="6" height="6" viewBox="0 0 6 6"><path d="M.5 3L3 .6 5.5 3v2.6h-5z" fill="none" stroke="#fff" stroke-width=".5"/></svg>About Us</li>
      <li style="padding-left:9px">Leadership</li><li style="padding-left:9px">Enterprise SAAS</li></ul></div>
    <div class="col" style="left:231px"><h5 style="margin-left:9px">Company</h5><ul>
      <li><svg width="6" height="6" viewBox="0 0 6 6"><rect x=".5" y=".5" width="5" height="5" fill="none" stroke="#fff" stroke-width=".5"/><path d="M1.5 4.5l3-3" stroke="#fff" stroke-width=".5"/></svg>Leadership</li>
      <li style="padding-left:9px">Blog</li><li style="padding-left:9px">Support</li></ul></div>
    <div class="col" style="left:318px"><h5>Helpful Links</h5><ul>
      <li><svg width="6" height="6" viewBox="0 0 6 6"><rect x=".8" y=".5" width="4.4" height="5" fill="none" stroke="#fff" stroke-width=".5"/></svg>Resource Center</li>
      <li style="padding-left:9px">API Documtntation</li><li style="padding-left:9px">Support</li></ul></div>
    <div class="col" style="left:405px"><h5>Newsletter Sign Up</h5><ul>
      <li><svg width="6" height="6" viewBox="0 0 6 6"><rect x=".5" y=".5" width="5" height="5" fill="none" stroke="#fff" stroke-width=".5"/></svg>Resource Center</li>
      <li style="padding-left:9px">API Documentation</li><li style="padding-left:9px">Partners</li>
      <li><svg width="6" height="6" viewBox="0 0 6 6"><rect x=".5" y=".5" width="5" height="5" fill="none" stroke="#fff" stroke-width=".5"/><path d="M1.5 3l1 1 2-2" fill="none" stroke="#fff" stroke-width=".5"/></svg>Privacy Policy</li>
      <li style="padding-left:9px">Terms of Service</li></ul></div>
    <div class="signup">
      <h5>Subcribe to Our Newsletter</h5>
      <div class="field">Enter your email...</div>
      <span class="go">SIGN UP</span>
      <div class="social"><span></span><span></span><span></span><span></span></div>
    </div>
    <div class="legal"><span>© 2024 Quorvel Brightmoss. All Rights Reserved.</span><span>hello@quorvelbrightmoss.com.au</span><span>Legal Notice</span></div>
  </footer>
</div>
</body>
</html>
```